We are looking for a clean new looking business card.

We would like a new, clean, and modern type business card with our updated contact information. We are a small a plumbing and heating and gasfitting company who offer 24 hr emergency service as well.
We feel our logo looks best on a white background.
Our current cards are outdated, both the design and the information.

Industry/Entity Type

Plumbing and heating

Contact Information for Business Card

Logo, Name, Title, Phone#, Email, Website, "24/7 Emergency Service"

Colors
0054AA
0677BA
7BADD7
CADEEF
E8F1F8

```html
<!DOCTYPE html>
<html lang="en">
<head>
<meta charset="UTF-8">
<title>clearflow – Business Card</title>
<link href="https://fonts.googleapis.com/css2?family=Tenor+Sans&display=swap" rel="stylesheet">
<style>
  :root {
    --blue-deep: #0054AA;
    --blue-mid: #0677BA;
    --blue-light: #7BADD7;
    --blue-pale: #CADEEF;
    --blue-mist: #E8F1F8;
    --ink: #4a4f55;
    --rule: #9aa0a6;
    --paper: #ffffff;
    --backdrop: #2e2f31;
  }
  * { margin: 0; padding: 0; box-sizing: border-box; }
  html, body { width: 1200px; height: 900px; overflow: hidden; }
  body {
    background: var(--backdrop);
    font-family: "Tenor Sans", sans-serif;
    position: relative;
  }
  .card {
    position: absolute;
    left: 320px;
    width: 560px;
    height: 320px;
    background: linear-gradient(160deg, var(--paper) 0%, #f3f5f7 100%);
    box-shadow: 0 8px 24px rgba(0,0,0,0.45);
    overflow: hidden;
  }
  .card-front { top: 95px; }
  .card-back { top: 485px; }

  .wordmark {
    position: absolute;
    display: flex;
    flex-direction: column;
  }
  .wordmark-row { display: flex; align-items: center; gap: 10px; }
  .wordmark-square {
    width: 26px; height: 26px;
    background: var(--blue-mid);
  }
  .wordmark-name {
    font-size: 46px;
    line-height: 1;
    color: var(--blue-deep);
    letter-spacing: 1px;
  }
  .wordmark-tagline {
    font-size: 9.5px;
    letter-spacing: 2px;
    color: #222;
    margin-top: 6px;
    margin-left: 36px;
    white-space: nowrap;
  }

  /* Front */
  .card-front .wordmark { left: 48px; top: 70px; }
  .accent-block {
    position: absolute;
    right: 0; top: 168px;
    width: 34px; height: 56px;
    background: var(--blue-deep);
  }
  .emergency {
    position: absolute;
    right: 54px; top: 172px;
    text-align: right;
  }
  .emergency-title {
    font-size: 25px;
    line-height: 1.2;
    color: var(--blue-deep);
  }
  .emergency-phone {
    font-size: 19px;
    color: var(--blue-light);
    margin-top: 4px;
    display: flex; align-items: center; justify-content: flex-end; gap: 6px;
  }

  /* Back */
  .identity { position: absolute; left: 40px; top: 96px; }
  .identity-name { font-size: 22px; color: var(--blue-light); }
  .identity-role { font-size: 14.5px; color: var(--ink); line-height: 1.45; margin-top: 4px; }

  .contact-list {
    position: absolute;
    left: 300px; top: 58px;
    list-style: none;
    font-size: 13.5px;
    color: var(--ink);
    line-height: 1.6;
  }
  .contact-list li { display: flex; align-items: flex-start; gap: 8px; }
  .contact-list svg { width: 12px; height: 12px; margin-top: 5px; flex: none; }
  .contact-list .indent { padding-left: 20px; }
  .contact-rule {
    position: absolute;
    left: 300px; right: 24px;
    height: 1px; background: var(--rule);
  }
  .contact-rule.bottom { top: 196px; }
  .card-back .wordmark { left: 300px; top: 214px; }
  .card-back .wordmark-name { font-size: 38px; }
  .card-back .wordmark-square { width: 22px; height: 22px; }
  .card-back .wordmark-tagline { font-size: 7.5px; margin-left: 32px; letter-spacing: 1.4px; }
</style>
</head>
<body>

<section class="card card-front">
  <div class="wordmark">
    <div class="wordmark-row">
      <span class="wordmark-square"></span>
      <span class="wordmark-name">clearflow</span>
    </div>
    <span class="wordmark-tagline">PLUMBING · HEATING · GASFITTING</span>
  </div>
  <div class="emergency">
    <p class="emergency-title">24/7 Emergency Service</p>
    <p class="emergency-phone">(555) 214-0368
      <svg width="18" height="16" viewBox="0 0 18 16" aria-hidden="true">
        <path d="M1 5c0-3 16-3 16 0v2h-4V5H5v2H1z" fill="var(--blue-deep)"/>
        <rect x="3" y="8" width="12" height="7" rx="1.5" fill="var(--blue-deep)"/>
      </svg>
    </p>
  </div>
  <div class="accent-block"></div>
</section>

<section class="card card-back">
  <div class="identity">
    <p class="identity-name">Marla Kensington</p>
    <p class="identity-role">Operations Manager<br>Apprentice Plumber and Gasfitter</p>
  </div>

  <ul class="contact-list">
    <li>
      <svg viewBox="0 0 12 12" aria-hidden="true"><path d="M0 4c0-2 12-2 12 0v1.5H9V4H3v1.5H0z M2 6h8v5H2z" fill="var(--blue-mid)"/></svg>
      (555) 214-0368
    </li>
    <li>
      <svg viewBox="0 0 12 12" aria-hidden="true"><rect x="0.5" y="2" width="11" height="8" rx="1" fill="var(--blue-mid)"/><path d="M1 3l5 4 5-4" stroke="#fff" fill="none"/></svg>
      info@clearflowpro.com
    </li>
    <li>
      <svg viewBox="0 0 12 12" aria-hidden="true"><circle cx="6" cy="6" r="5" fill="none" stroke="var(--blue-mid)" stroke-width="1.4"/><path d="M1 6h10M6 1c-2.5 3-2.5 7 0 10M6 1c2.5 3 2.5 7 0 10" stroke="var(--blue-mid)" fill="none"/></svg>
      www.clearflowpro.com
    </li>
    <li>
      <svg viewBox="0 0 12 12" aria-hidden="true"><path d="M6 0.5a4 4 0 0 1 4 4c0 3-4 7-4 7s-4-4-4-7a4 4 0 0 1 4-4z" fill="var(--blue-mid)"/><circle cx="6" cy="4.5" r="1.5" fill="#fff"/></svg>
      18 Harbour Ridge Way SE
    </li>
    <li class="indent">Westfield, AB T0X 4Z2, Canada</li>
  </ul>
  <div class="contact-rule bottom"></div>

  <div class="wordmark">
    <div class="wordmark-row">
      <span class="wordmark-square"></span>
      <span class="wordmark-name">clearflow</span>
    </div>
    <span class="wordmark-tagline">PLUMBING · HEATING · GASFITTING</span>
  </div>
</section>

</body>
</html>
```